依頼詳細
川辺ふれあい会の第7号の会報の原稿を依頼する。この活動を行うボランティア募集案内で①福祉車両、買い物、病院送迎ボランティア募集 ②子ども食堂開催の際のボランティア募集 ③夏季の子ども学習指導、ゲームや遊びボランティア募集 ④高齢者居場所づくりのサロンの話し相手のボランティア募集 ⑤生活支援の一般ボランティア募集(くさとり、清掃、片付けなど)のボランテイア募集の会報の編集依頼

記載項目
デザインを見てから、説明文は後日指示します。
サイズ
A4
ページ数
片面
希望イメージ
シンプル 複雑
単色 カラフル
暗い 明るい
日常 高級
遊び心 厳粛
未来的 伝統的
女性的 男性的
希望する色
青系
納品ファイル
• 高解像度JPG (.jpg)
補足説明
データをいただき、説明文の追加等を加筆し原稿をPDFにして印刷業者へ依頼する。

```html
<!DOCTYPE html>
<html lang="ja">
<head>
<meta charset="utf-8">
<title>川辺ふれあい会 会報 第7号</title>
<link href="https://fonts.googleapis.com/css2?family=M+PLUS+Rounded+1c:wght@500;800;900&family=Noto+Sans+JP:wght@400;700;900&display=swap" rel="stylesheet">
<style>
:root{
  --blue:#1c5fb8;
  --blue-dark:#123f86;
  --blue-pale:#e6f0fb;
  --pink:#e8407a;
  --pink-pale:#fbd8e4;
  --orange:#f08a1c;
  --yellow:#fff27a;
  --yellow-pale:#fff7c8;
  --green:#3aa547;
  --green-pale:#d9f0d2;
  --purple:#8a4cc2;
  --purple-pale:#eadcf6;
  --ink:#333;
  --photo:#cfd3d8;
  --photo-text:#555;
}
*{box-sizing:border-box;margin:0;padding:0}
html,body{width:851px;height:1200px;overflow:hidden;background:#fff}
body{font-family:"Noto Sans JP",sans-serif;color:var(--ink)}
.sheet{position:relative;width:851px;height:1200px;background:linear-gradient(#fff 0,#fff 70%,var(--blue-pale) 100%);overflow:hidden}
.abs{position:absolute}

.org-label{left:40px;top:52px;padding:4px 16px;border:3px solid var(--blue);border-radius:14px;color:var(--blue);font:900 34px "M PLUS Rounded 1c",sans-serif;background:#fff}
.org-name{left:36px;top:108px;color:var(--blue);font:900 92px/1 "M PLUS Rounded 1c",sans-serif;letter-spacing:2px}
.issue{right:30px;top:30px;font-size:14px;color:var(--ink)}
.badge{left:660px;top:84px;width:160px;height:118px;border:4px solid var(--blue);border-radius:12px;background:#fff;display:flex;align-items:center;justify-content:center;gap:6px;color:var(--blue);white-space:nowrap}
.badge .kaiho{writing-mode:vertical-rl;font:800 20px/1 "M PLUS Rounded 1c",sans-serif}
.badge .num{display:flex;align-items:flex-end;font:900 30px/1 "M PLUS Rounded 1c",sans-serif;white-space:nowrap}
.badge .num b{font-size:84px;line-height:.9;margin:0 2px}

.band{left:0;top:222px;width:851px;height:28px;background:var(--blue);color:#fff;font-size:13px;display:flex;align-items:center;padding:0 34px;gap:40px;white-space:nowrap}

.lead{left:0;top:262px;width:851px;text-align:center;color:var(--blue-dark);font:900 34px "M PLUS Rounded 1c",sans-serif}
.lead::after{content:"";display:block;width:340px;height:5px;margin:2px auto 0;background:var(--pink);border-radius:3px}
.headline{left:0;top:306px;width:851px;text-align:center}
.headline span{display:inline-block;padding:0 18px;background:linear-gradient(transparent 55%,var(--yellow) 55%);color:var(--pink);font:900 64px/1.1 "M PLUS Rounded 1c",sans-serif}
.intro{left:50px;top:384px;width:760px;font-size:17px;line-height:1.55;color:var(--ink);font-weight:700}
.intro small{font-size:15px;font-weight:400}

.blob{border-radius:50%}
.cat{white-space:nowrap}
.cat-title{font:900 38px/1 "M PLUS Rounded 1c",sans-serif}
.cat-title em{font-style:normal;font-size:22px;color:var(--ink)}
.cat-sub{font:900 24px/1.2 "M PLUS Rounded 1c",sans-serif;color:var(--ink);margin-top:6px}
.cat-desc{font-size:14px;font-weight:700;color:var(--ink);line-height:1.45;margin-top:6px}
.photo{background:var(--photo);display:flex;align-items:center;justify-content:center;color:var(--photo-text);font-weight:700;font-size:22px;border:3px solid #fff}
.art{border-radius:18px}

.call{left:330px;top:690px;width:190px;height:64px;border:3px dashed var(--blue);border-radius:34px;background:#fff;color:var(--blue);font:800 13px/1.4 "M PLUS Rounded 1c",sans-serif;text-align:center;display:flex;align-items:center;justify-content:center;white-space:nowrap}

.notes{left:210px;top:988px;width:530px;height:196px;color:var(--blue-dark);font-size:14.2px;line-height:1.7;letter-spacing:1px;overflow:hidden;word-break:break-all}
.vert{left:752px;top:990px;width:70px;height:194px;border:3px solid var(--blue);border-radius:8px;background:#fff;color:var(--blue);display:flex;align-items:center;justify-content:center}
.vert span{writing-mode:vertical-rl;font:900 26px/1 "M PLUS Rounded 1c",sans-serif;letter-spacing:4px;white-space:nowrap}
</style>
</head>
<body>
<main class="sheet">
  <div class="abs org-label">NPO法人川辺</div>
  <h1 class="abs org-name">ふれあい会</h1>
  <p class="abs issue">2022. 2. 21発行</p>
  <div class="abs badge"><span class="kaiho">会報</span><span class="num">第<b>7</b>号</span></div>

  <div class="abs band"><span>会員・ボランティアを募集中！事務局までお気軽にお問い合わせください。</span><span>発行責任者　事務局</span></div>

  <p class="abs lead">あなたも参加できる</p>
  <h2 class="abs headline"><span>ボランティア募集中!</span></h2>
  <p class="abs intro">川辺地区にお住まいの、困っている方・手助けが必要な方への支援ボランティアを募集します。<br><small>高齢化社会になり、体力の衰えや日常生活に支障をきたして困っている人たちが増えています。<br>ボランティア内容は、どなたでもできる簡単な作業です。内容と場所・時間帯を自由に選んで活動できます。</small></p>

  <div class="abs blob" style="left:20px;top:460px;width:300px;height:260px;background:var(--purple-pale)"></div>
  <div class="abs blob" style="left:270px;top:455px;width:300px;height:250px;background:var(--yellow-pale)"></div>
  <div class="abs blob" style="left:540px;top:460px;width:300px;height:260px;background:var(--pink-pale)"></div>
  <div class="abs blob" style="left:30px;top:735px;width:330px;height:250px;background:var(--yellow-pale)"></div>
  <div class="abs blob" style="left:430px;top:730px;width:390px;height:260px;background:var(--green-pale)"></div>

  <!-- 学習 -->
  <div class="abs cat" style="left:70px;top:478px">
    <p class="cat-title" style="color:var(--purple)">学習<em>ボランティア</em></p>
    <p class="cat-desc">夏季の子ども学習指導<br>ゲームや遊び 等</p>
  </div>
  <div class="abs art" role="img" aria-label="子どもに勉強を教えるイラスト" style="left:205px;top:540px;width:85px;height:105px;background:#d9c3ef"></div>
  <div class="abs photo" role="img" aria-label="学習ボランティアの写真" style="left:55px;top:600px;width:175px;height:95px">写真等</div>

  <!-- 送迎 -->
  <div class="abs cat" style="left:322px;top:470px">
    <p class="cat-title" style="color:var(--orange)">送迎<em>ボランティア</em></p>
    <p class="cat-desc">福祉車両・買い物・病院送迎 等</p>
  </div>
  <div class="abs art" role="img" aria-label="福祉車両で送迎するイラスト" style="left:300px;top:545px;width:245px;height:130px;background:linear-gradient(#fbe3b5,#f6c97e)"></div>

  <!-- 子ども食堂 -->
  <div class="abs cat" style="left:585px;top:480px">
    <p class="cat-title" style="color:var(--pink)">子ども食堂</p>
    <p class="cat-sub">ボランティア</p>
    <p class="cat-desc">子ども食堂開催の際</p>
  </div>
  <div class="abs art" role="img" aria-label="食事をする子どものイラスト" style="left:570px;top:605px;width:80px;height:100px;background:#f7c0d2"></div>
  <div class="abs photo" role="img" aria-label="子ども食堂ボランティアの写真" style="left:650px;top:608px;width:175px;height:97px">写真等</div>

  <div class="abs call">手助けしていただける方<br>お待ちしています！</div>

  <!-- サロン -->
  <div class="abs cat" style="left:200px;top:762px">
    <p class="cat-title" style="color:var(--blue)">サロン</p>
    <p class="cat-sub">ボランティア</p>
    <p class="cat-desc">高齢者居場所づくりの<br>サロンの話し相手 等</p>
  </div>
  <div class="abs art" role="img" aria-label="高齢者と話すイラスト" style="left:50px;top:755px;width:135px;height:120px;background:#f3e3a8"></div>
  <div class="abs photo" role="img" aria-label="サロンボランティアの写真" style="left:110px;top:895px;width:200px;height:82px">写真等</div>

  <!-- 日常支援 -->
  <div class="abs cat" style="left:460px;top:755px">
    <p class="cat-title" style="color:var(--green)">日常支援</p>
    <p class="cat-sub">ボランティア</p>
    <p class="cat-desc">生活支援の一般ボランティア<br>草取り・清掃・片付け 等</p>
  </div>
  <div class="abs art" role="img" aria-label="草取りや清掃をするイラスト" style="left:685px;top:760px;width:115px;height:100px;background:#bfe3b4"></div>
  <div class="abs photo" role="img" aria-label="日常支援ボランティアの写真" style="left:545px;top:885px;width:210px;height:92px">写真等</div>

  <!-- bottom -->
  <div class="abs photo" role="img" aria-label="活動の写真" style="left:35px;top:988px;width:160px;height:196px;border-color:var(--photo)">写真等</div>
  <p class="abs notes">あああああああああああああああああああああああああああああああああああああああああああああああああああああああああああああああああああああああああああああああああああああああああああああああああああああああああああああああああああああああああああああああああああああああああああああああああああああああああああああああああああああああああああああああああああああああああああああああああああああああああああああああああああああああああああああああああああああああああああああああああああああああああああああああああああああああああああああああああああああああああああ</p>
  <div class="abs vert"><span>あああああ</span></div>
</main>
</body>
</html>
```